Wheatless Table Co Web Design

We are looking for designs for a homepage for a gluten free, health food website.

We are looking for the site to be a shop, as well as a resource/information source for users. We will also look to incorporate recipes, blogs, forums and potentially some other useful information.

We want to ensure that the website is user-friendly, does not have a corporate feel, but is still classy.

We want to have high quality photographic images in the background, with text in the foreground - but these things will need to compliment each other well. e.g recipe of the week integrated onto the background photo and the 'shop' in the foreground.

We have seen a site that we quite like and although we like the design, we do not want to completely emulate this. However, it is a useful starting point for designers and perhaps some inspiration www.brambleharvestgrocer.example

We already have a logo - see attached - which will need to be fully integrated into the design.

We do want a colourful design, but mainly in terms of the images rather than the graphics.
Updates

Please note:

We are pleased with the designs to date, for the most part. We would like you all to note, however, that we are much preferring the lighter designs - ones that make the sites feel brighter - rather than those which are darker in appearance.

We would also like to see less space allocated to the main image, within the context of the site as a whole.

Thanks.

We have eliminated those which we feel are not what we are looking for. We are still keen to see some more designs and are still looking for something unique. There are some good things in all of the designs that we have not eliminated, however we still feel there is room for more inspiration.

Thanks.

Target Market(s)

Our audience are body conscience people looking for health food products. They are also those who are potentially looking for a new lifestyle/life cha

Industry/Entity Type

Health

Requirements
Must have
• Our logo - attached, can provide variations in due course.

Navigational features as per mock up attached.

Social network integration.

NB: we only need one (home) page for this.

```html
<!DOCTYPE html>
<html lang="en">
<head>
<meta charset="utf-8">
<title>Wheatless Table Co</title>
<link href="https://fonts.googleapis.com/css2?family=Raleway:wght@300;400;500;600&family=Arvo:wght@400;700&family=Lora:ital@0;1&family=Dancing+Script:wght@500&display=swap" rel="stylesheet">
<style>
:root{
  --ink:#1f1f1f;
  --soft:#6e6e6e;
  --red:#c3000e;
  --green:#62a531;
  --blue:#2a9ce0;
  --orange:#e4662c;
  --wood:#e9dcc7;
  --wood-dark:#d8c6a9;
  --footer:#efebe3;
  --white:#ffffff;
  --dark:#141414;
  --social:#5aa632;
}
*{box-sizing:border-box;margin:0;padding:0}
html,body{width:859px;height:1200px;overflow:hidden}
body{position:relative;font-family:"Raleway",sans-serif;color:var(--ink);background:linear-gradient(180deg,var(--wood) 0%,var(--wood-dark) 50%,var(--wood) 100%)}
.abs{position:absolute}
.hero{left:0;top:0;width:859px;height:418px;background:radial-gradient(ellipse at 40% 35%,#c9b8a0 0%,#8a6848 30%,#5b3d26 60%,#3a281a 100%)}
.hero-green{left:0;top:0;width:250px;height:418px;background:linear-gradient(160deg,rgba(90,140,90,.75),rgba(90,140,90,0) 80%)}
.topbar{left:0;top:0;width:859px;height:33px;background:rgba(255,255,255,.72)}
.brand{left:20px;top:11px;height:26px;display:flex;align-items:center;gap:6px;font-weight:600;font-size:12px;color:var(--dark)}
.brand-mark{width:14px;height:14px;background:var(--dark)}
.nav{top:12px;left:513px;display:flex;gap:0;font-size:7px;font-weight:600;text-transform:uppercase;letter-spacing:.2px}
.nav a{position:absolute;white-space:nowrap;color:var(--dark);text-decoration:none}
.search{left:662px;top:6px;width:136px;height:19px;background:var(--white);font-family:"Lora",serif;font-style:italic;font-size:7px;color:#bbb;padding:5px 6px}
.search-btn{left:798px;top:6px;width:44px;height:19px;background:var(--dark);color:var(--white);font-size:8px;font-weight:600;text-align:center;line-height:19px}
.side{left:0;top:110px;width:90px;height:152px;background:rgba(0,0,0,.85);border:1.5px dashed rgba(255,255,255,.85);border-left:none;border-radius:0 4px 4px 0}
.side a{position:absolute;left:19px;font-size:8px;color:var(--white);text-decoration:none}
.headline{left:0;width:859px;top:118px;text-align:center;font-family:"Arvo",serif;font-weight:700;font-size:35px;color:#f3efe8;letter-spacing:1px;text-shadow:0 2px 4px rgba(0,0,0,.5)}
.sub{left:0;width:859px;top:172px;text-align:center;font-family:"Dancing Script",cursive;font-size:20px;color:var(--white);text-shadow:0 1px 3px rgba(0,0,0,.5)}
.learn{left:402px;top:218px;width:95px;height:25px;background:var(--white);border:1px solid var(--dark);outline:2px solid var(--white);font-family:"Lora",serif;font-style:italic;font-size:10px;text-align:center;line-height:23px}
.arrow{top:166px;width:30px;height:30px;border-radius:50%;background:rgba(255,255,255,.9)}
.card{top:305px;width:175px;height:212px;background:rgba(255,255,255,.82);text-align:center}
.card-img{position:absolute;left:7px;top:10px;width:161px;height:95px;border:1px solid #ddd}
.card-kicker{position:absolute;top:128px;width:100%;font-size:11.5px;font-weight:500}
.card-word{position:absolute;top:140px;width:100%;font-family:"Arvo",serif;font-weight:700;font-size:24px;letter-spacing:1px}
.card-btn{position:absolute;left:50px;top:179px;width:74px;height:22px;background:var(--dark);color:var(--white);font-family:"Lora",serif;font-style:italic;font-size:12px;line-height:22px}
.store-badge{position:absolute;left:52px;top:179px;width:73px;height:22px;background:var(--dark);border-radius:3px}
.stickers{left:312px;top:524px;width:276px;height:76px;background:linear-gradient(90deg,#4a3a8a 0 30%,#c98c3c 30% 62%,#f2e6a0 62% 100%);border-radius:30px 30px 0 0;opacity:.9}
.panel{left:113px;top:600px;width:630px;height:438px;background:var(--white)}
.panel-mark{position:absolute;left:272px;top:24px;width:86px;text-align:center}
.panel-mark .dot{width:58px;height:58px;border-radius:50%;background:var(--dark);margin:0 auto 4px}
.panel-mark span{font-size:9px;font-weight:600;color:var(--dark)}
.panel h1{position:absolute;top:110px;width:100%;text-align:center;font-weight:300;font-size:24px;color:var(--dark)}
.panel .lead{position:absolute;top:144px;width:100%;text-align:center;font-family:"Lora",serif;font-style:italic;font-size:9.5px;color:var(--soft)}
.panel .rule{position:absolute;left:11px;top:167px;width:602px;height:1px;background:#ddd}
.panel h2{position:absolute;top:193px;font-weight:400;font-size:15.5px;text-transform:uppercase;color:var(--dark)}
.recipe{position:absolute;top:232px;width:126px;height:190px;background:#f6f4f1;text-align:center}
.recipe-img{height:85px}
.recipe h3{font-size:10px;font-weight:500;margin-top:12px;padding:0 4px;text-align:left;white-space:nowrap;overflow:hidden}
.recipe p{font-family:"Lora",serif;font-style:italic;font-size:7.8px;color:#999;text-align:left;padding:4px 6px 0 7px;line-height:9.6px}
.recipe .view{position:absolute;left:27px;top:162px;width:63px;height:18px;background:var(--red);color:var(--white);font-size:8px;line-height:18px}
.post{position:absolute;left:423px;width:200px}
.post .avatar{position:absolute;left:0;top:2px;width:36px;height:36px;border-radius:50%;background:#3a3a3a}
.post p{position:absolute;left:51px;width:140px;font-size:8.5px;color:#777;line-height:11.2px}
.post small{position:absolute;left:51px;top:46px;font-size:6.5px;color:var(--red)}
.footer{left:0;top:1080px;width:859px;height:120px;background:var(--footer)}
.flinks a{position:absolute;font-size:7px;font-weight:500;text-transform:uppercase;color:var(--dark);text-decoration:none}
.email{left:378px;top:1108px;width:179px;height:24px;background:var(--white);border:1px solid #ddd;font-size:7px;color:#999;padding:8px 7px}
.join{left:522px;top:1111px;width:30px;height:17px;background:var(--red);color:var(--white);font-size:8px;text-align:center;line-height:17px}
.social{top:1113px;width:16px;height:16px;border-radius:50%;background:var(--social)}
.copy{right:133px;top:1170px;font-size:7px;color:var(--dark)}
</style>
</head>
<body>
<div class="abs hero" role="img" aria-label="Photograph of tea cups, cookies, pistachios and coffee beans on a rustic wooden table"></div>
<div class="abs hero-green" aria-hidden="true"></div>

<header class="abs topbar"></header>
<div class="abs brand"><span class="brand-mark"></span>Wheatless Table Co</div>
<nav class="abs nav" style="left:0;width:859px">
  <a style="left:513px">Home</a>
  <a style="left:554px">Login</a>
  <a style="left:596px">Contact Us</a>
</nav>
<div class="abs search">Enter Key Words</div>
<div class="abs search-btn">Submit</div>

<nav class="abs side">
  <a style="top:12px">Shop</a>
  <a style="top:35px">Our Story</a>
  <a style="top:58px">Blog</a>
  <a style="top:80px">Hints &amp; Tips</a>
  <a style="top:103px">Recipies</a>
  <a style="top:126px">Forums</a>
</nav>

<div class="abs headline">Neque porro quisquam est.</div>
<div class="abs sub">Lorem ipsum dolor sit amet, consectetur adipiscing elit.</div>
<div class="abs learn">Learn More &#8594;</div>
<svg class="abs arrow" style="left:105px" viewBox="0 0 30 30"><path d="M17 9l-6 6 6 6" fill="none" stroke="#222" stroke-width="3"/></svg>
<svg class="abs arrow" style="left:727px" viewBox="0 0 30 30"><path d="M13 9l6 6-6 6" fill="none" stroke="#222" stroke-width="3"/></svg>

<section class="abs card" style="left:114px">
  <div class="card-img" role="img" aria-label="Photograph of a grocery produce display" style="background:linear-gradient(135deg,#7a5a2a,#c2693a,#9aa24a)"></div>
  <div class="card-kicker">Find Your Nearest</div>
  <div class="card-word" style="color:var(--green)">STORE</div>
  <div class="card-btn">Find Now</div>
</section>
<section class="abs card" style="left:338px">
  <div class="card-img" role="img" aria-label="Photograph of two young cooks in chef hats" style="background:linear-gradient(135deg,#8a7060,#e8e0d8,#b23a30)"></div>
  <div class="card-kicker">Look For Tasty</div>
  <div class="card-word" style="color:var(--blue)">RECIPIES</div>
  <div class="card-btn">Find Now</div>
</section>
<section class="abs card" style="left:567px">
  <div class="card-img" role="img" aria-label="Illustration of a phone showing the mobile app" style="background:linear-gradient(90deg,#eee 0 40%,#1e7fa0 40% 50%,#eee 50%)"></div>
  <div class="card-kicker">Download Mobile App</div>
  <div class="card-word" style="color:var(--orange)">PocketApp</div>
  <div class="store-badge" aria-label="AppShelf download badge"></div>
</section>

<div class="abs stickers" role="img" aria-label="Illustrated stickers of grapes, a bread basket and cheese"></div>

<main class="abs panel">
  <div class="panel-mark"><div class="dot"></div><span>Wheatless Table Co</span></div>
  <h1>Neque porro quisquam est qui dolorem ipsum quia</h1>
  <p class="lead">Lorem ipsum dolor sit amet, consectetur adipiscing elit. Cras id feugiat nulla, id sodales urna.</p>
  <div class="rule"></div>
  <h2 style="left:17px">Today's Popular Receipies</h2>
  <h2 style="left:423px">Latest Discussions</h2>

  <article class="recipe" style="left:15px">
    <div class="recipe-img" role="img" aria-label="Photograph of a fresh vegetable salad" style="background:linear-gradient(135deg,#3f7a2a,#c9d6b0,#c2361e)"></div>
    <h3>Neque porro quisquam...</h3>
    <p>Lorem ipsum dolor sit amet, consectetur adipisc-ing elit. Cras id feugiat nulla, id sodales urna.</p>
    <div class="view">VIEW</div>
  </article>
  <article class="recipe" style="left:145px">
    <div class="recipe-img" role="img" aria-label="Photograph of grilled meat and vegetables" style="background:linear-gradient(135deg,#3b2a1e,#8a5a30,#b2462a)"></div>
    <h3>Neque porro quisquam...</h3>
    <p>Lorem ipsum dolor sit amet, consectetur adipisc-ing elit. Cras id feugiat nulla, id sodales urna.</p>
    <div class="view">VIEW</div>
  </article>
  <article class="recipe" style="left:276px">
    <div class="recipe-img" role="img" aria-label="Photograph of bacon-wrapped appetizers" style="background:linear-gradient(135deg,#8a2a18,#d0784a,#a0401e)"></div>
    <h3>Neque porro quisquam...</h3>
    <p>Lorem ipsum dolor sit amet, consectetur adipisc-ing elit. Cras id feugiat nulla, id sodales urna.</p>
    <div class="view">VIEW</div>
  </article>

  <div class="post" style="top:228px"><div class="avatar"></div><p>Lorem ipsum dolor sit amet, con-sectetur adipiscing elit. Cras id feugiat nulla, id sodales urna.</p><small>Posted On 06062013</small></div>
  <div class="post" style="top:296px"><div class="avatar"></div><p>Lorem ipsum dolor sit amet, con-sectetur adipiscing elit. Cras id feugiat nulla, id sodales urna.</p><small>Posted On 06062013</small></div>
  <div class="post" style="top:364px"><div class="avatar"></div><p>Lorem ipsum dolor sit amet, con-sectetur adipiscing elit. Cras id feugiat nulla, id sodales urna.</p><small>Posted On 06062013</small></div>
</main>

<footer class="abs footer"></footer>
<nav class="flinks">
  <a style="left:116px;top:1107px">About Us</a>
  <a style="left:116px;top:1121px">Careers</a>
  <a style="left:116px;top:1136px">Contact Us</a>
  <a style="left:116px;top:1150px">Coupons</a>
  <a style="left:116px;top:1165px">Gift Cards</a>
  <a style="left:280px;top:1107px">Forums</a>
  <a style="left:280px;top:1121px">Privacy</a>
  <a style="left:280px;top:1136px">Terms</a>
</nav>
<div class="abs email">JOIN OUR EMAIL LIST</div>
<div class="abs join">JOIN</div>
<div class="abs social" style="left:658px"></div>
<div class="abs social" style="left:675px"></div>
<div class="abs social" style="left:693px"></div>
<div class="abs social" style="left:711px"></div>
<div class="abs copy">&copy; 2013 Wheatless Table Co, LLC. All Rights Reserved.</div>
</body>
</html>
```